Business Consulting Company requires a website design (PSD+HTML+CSS required)

Tarnvale Advisory is a Business Consulting Company that provides Analysis, Business Coaching and Systems and Document Design for clients.

We would like a simplistic yet professional looking website design that uses high quality imagery to project a professional persona across our entire site.

The completed project will need to include PSD files (for editing in Photoshop) and will need to also include HTML+CSS coded files that can be edited in Adobe Dreamweaver CS5.5.

Tarnvale Advisory currently has a functioning website (located at www.tarnvaleadvisory.com.au) but would like to replace its current site with something more professional, user friendly and content simplistic, with the overall design of this project being clean and very easy to navigate whilst remaining professionally focused.

A brief has been attached to this project to provide the key details but please feel free to contact me if you require any clarification or have any questions regarding the project.

Target Market(s)

The target audience for this website will be small to medium sized businesses (of all descriptions).

Industry/Entity Type

Business

Coding

Coded - Design and coding required

Number of Pages Required

5+ page

Requirements
Must have
• Simplistic design structure
• Professional images
• Easy to navigate
• Must be uploaded in PSD format
• Must be coded (HTML+CSS) and compatible with Adobe Dreamweaver CS5.5
Nice to have
• Use of the Company’s corporate colours throughout the site design
• Adding a Home page slider bar with images and short catchy messages (i.e. text based statements)
• Having a quick link box on each page that provides easy navigation throughout the site
• The use of different icons and images to depict our different services (i.e. a different icon and image for analysis service and coaching service etc.).
• All pages should follow a similar theme (universal approach to all pages)
Should not have
• When coding, images should not be used in place of text (all text must be editable)

```html
<!DOCTYPE html>
<html lang="en">
<head>
<meta charset="utf-8">
<title>Tarnvale Advisory</title>
<link href="https://fonts.googleapis.com/css2?family=Open+Sans:ital,wght@0,400;0,600;1,400&family=Raleway:wght@400;500&family=Montserrat:wght@600&family=Oswald:wght@500&family=Arimo:wght@400;700&display=swap" rel="stylesheet">
<style>
:root{
  --blue:#0099d9;
  --blue-dark:#0a7fb5;
  --ink:#222;
  --text:#666;
  --muted:#888;
  --page:#f9f9f9;
  --card:#f3f4f8;
  --footer:#2b2b2b;
  --footer-bar:#555;
  --nav-active:#5a5a5a;
}
*{box-sizing:border-box;margin:0;padding:0}
html,body{width:1200px;height:2378px;overflow:hidden}
body{position:relative;background:var(--page);font-family:"Open Sans",sans-serif;color:var(--text)}
.abs{position:absolute}

/* header */
.site-header{left:0;top:0;width:1200px;height:135px;background:#fff}
.brand{left:98px;top:46px;display:flex;align-items:center;gap:14px}
.brand-mark{width:46px;height:46px;border-radius:50%;border:7px solid #555}
.brand-name{font-family:"Arimo",sans-serif;font-size:30px;font-weight:400;color:#555;letter-spacing:1px}
.search{left:567px;top:60px;width:233px;height:29px;border:1px solid #ddd;background:#fff;font-size:11px;color:#999;padding:7px 8px}
.search svg{position:absolute;right:8px;top:7px}
.contact-label{left:843px;top:32px;font-family:"Arimo",sans-serif;font-size:21px;color:#222}
.contact-call{left:843px;top:62px;display:flex;align-items:center;gap:10px;font-family:"Arimo",sans-serif;font-size:24px;font-weight:700}
.contact-call .call{color:var(--blue)}
.contact-call .num{color:#bbb}

/* nav */
.main-nav{left:0;top:135px;width:1200px;height:52px;background:var(--blue)}
.main-nav a{position:absolute;top:15px;font-family:"Arimo",sans-serif;font-size:14px;color:#fff;text-decoration:none}
.main-nav .active{left:100px;top:7px;width:96px;height:37px;background:var(--nav-active);border-radius:2px;text-align:center;line-height:37px}

/* hero */
.hero{left:0;top:187px;width:1200px;height:534px;background:linear-gradient(100deg,#c9cdd2 0%,#7d8a96 30%,#2f3b4f 50%,#d8dce2 75%,#eef0f3 100%)}
.quote-form{left:342px;top:555px;display:flex}
.quote-input{width:374px;height:52px;background:#fff;font-size:20px;color:#aaa;padding:13px 14px}
.quote-btn{width:175px;height:52px;background:#4a4a4a;border:2px solid #ddd;color:#fff;font-size:20px;text-align:center;line-height:48px}

/* intro band */
.intro{left:0;top:721px;width:1200px;height:194px;background:var(--blue);color:#fff;text-align:center}
.intro h1{font-family:"Raleway",sans-serif;font-weight:400;font-size:25px;margin-top:26px;letter-spacing:.3px}
.intro p{font-family:"Arimo",sans-serif;font-size:14px;line-height:20px;width:1060px;margin:14px auto 0}
.intro-pointer{left:588px;top:915px;width:0;height:0;border-left:12px solid transparent;border-right:12px solid transparent;border-top:14px solid var(--blue)}

/* iconboxes */
.iconbox{top:983px;width:340px}
.iconbox .ring{position:absolute;left:0;top:0;width:73px;height:73px;border-radius:50%;border:1px solid var(--blue);display:flex;align-items:center;justify-content:center}
.iconbox h3{position:absolute;left:95px;top:2px;font-family:"Montserrat",sans-serif;font-size:16px;color:#222;letter-spacing:1.2px}
.iconbox p{position:absolute;left:95px;top:28px;width:255px;font-size:13px;line-height:21px;color:#777}

/* service cards */
.card{top:1186px;height:304px;background:var(--card)}
.card .photo{position:absolute;left:0;top:0;width:100%;height:142px}
.card .badge{position:absolute;left:50%;top:107px;width:73px;height:73px;margin-left:-36px;background:var(--blue);display:flex;align-items:center;justify-content:center}
.card h4{position:absolute;left:0;top:200px;width:100%;text-align:center;font-weight:400;font-size:17px;color:#555}
.card p{position:absolute;left:30px;right:30px;top:237px;text-align:center;font-size:12px;line-height:20px;color:#999}

/* testimonial */
.testimonial{left:114px;top:1628px;width:358px;height:345px;background:#fff;box-shadow:0 1px 6px rgba(0,0,0,.18);border-radius:3px;text-align:center}
.avatar{left:228px;top:1581px;width:112px;height:112px;border-radius:50%;border:3px solid #1c4f86;background:radial-gradient(circle at 50% 40%,#d9b49a,#8a6a58 70%,#3a3f4f)}
.testimonial h5{margin-top:84px;font-family:"Arimo",sans-serif;font-size:15px;color:#1c4f86;font-weight:700}
.testimonial p{margin:18px 28px 0;font-style:italic;font-size:14.5px;line-height:24.5px;color:#888}

/* process */
.step-ring{left:534px;width:95px;height:95px;border-radius:50%;border:2px solid #e2e2e2;background:#fff;display:flex;align-items:center;justify-content:center}
.step-line{left:580px;top:1688px;width:0;height:210px;border-left:1px dashed #ddd}
.step{left:656px;width:442px}
.step h4{font-weight:400;font-size:19px;color:#222}
.step p{margin-top:10px;font-size:12.5px;line-height:20px;color:#666}

/* footer */
.site-footer{left:0;top:2064px;width:1200px;height:269px;background:var(--footer);color:#aaa}
.site-footer h2{position:absolute;top:48px;font-family:"Oswald",sans-serif;font-weight:500;font-size:24px;color:#fff;letter-spacing:.5px}
.news-text{left:114px;top:90px;width:320px;font-size:12px;line-height:20px;color:#888}
.news-form{left:114px;top:128px;display:flex}
.news-input{width:215px;height:37px;background:#fff;font-size:12px;color:#999;padding:10px 12px}
.news-btn{width:74px;height:37px;background:var(--blue);color:#fff;font-size:12px;font-weight:600;text-align:center;line-height:37px}
.social{left:114px;top:193px;display:flex;gap:10px}
.social span{width:40px;height:40px;border-radius:50%;border:1px solid #777}
.loc{left:515px;display:flex;gap:12px;font-size:12.5px;line-height:20px;color:#bbb}
.tweet-dot{left:925px;top:85px;width:30px;height:30px;border-radius:50%;background:#fff}
.tweet{left:864px;top:124px;width:185px;font-size:12.5px;line-height:20px;color:#aaa}
.tweet-meta{left:866px;top:220px;width:165px;display:flex;justify-content:space-between;font-size:12.5px;color:#fff}
.copyright{left:0;top:2333px;width:1200px;height:45px;background:var(--footer-bar);color:#fff;font-family:"Arimo",sans-serif;font-size:13px;text-align:center;line-height:45px}
</style>
</head>
<body>

<header class="site-header abs">
  <div class="brand abs"><span class="brand-mark"></span><span class="brand-name">Tarnvale Advisory</span></div>
  <div class="search abs">Search here...
    <svg width="14" height="14" viewBox="0 0 14 14"><circle cx="6" cy="6" r="4.5" fill="none" stroke="#888" stroke-width="1.6"/><line x1="9.3" y1="9.3" x2="13" y2="13" stroke="#888" stroke-width="1.8"/></svg>
  </div>
  <div class="contact-label abs">Contact Us Now</div>
  <div class="contact-call abs">
    <svg width="26" height="26" viewBox="0 0 26 26"><circle cx="13" cy="13" r="13" fill="var(--blue)"/><path d="M9 7c1 0 2 2 2 3s-1 1-1 2c1 2 2 3 4 4 1 0 1-1 2-1s3 1 3 2-1 3-3 3c-5 0-10-5-10-10 0-2 2-3 3-3z" fill="#fff"/></svg>
    <span class="call">Call !!</span><span class="num">08 5550 1827</span>
  </div>
</header>

<nav class="main-nav abs">
  <a class="active" href="#">HOME</a>
  <a href="#" style="left:214px">ABOUT US</a>
  <a href="#" style="left:336px">CAPABILITIES</a>
  <a href="#" style="left:480px">MISSION</a>
  <a href="#" style="left:587px">NEWS</a>
  <a href="#" style="left:678px">PHOTOS</a>
  <a href="#" style="left:785px">CONTACT</a>
</nav>

<section class="hero abs" role="img" aria-label="Photo of smiling business people shaking hands around a meeting table with a laptop"></section>
<div class="quote-form abs"><div class="quote-input">Email Address...</div><div class="quote-btn">Request a Quote</div></div>

<section class="intro abs">
  <h1>LOREM IPSUM IS SIMPLY DUMMY TEXT OF THE PRINTING ...</h1>
  <p>Vestibululis lacinia est. Proin dictum elementum velit. Fusce euismod consequat ante. Lorem ipsum dolor sit amet, constetuer adipiscing elit. Pelleesque sed dolor. Aliquam congue. Vestibululis lacinia est. Proin dictum elementum velit.Lorem ipsum dolor sit amet, consectetuer adipiscing elit. Aenean commodo ligula eget dolor. Aenean massa. Cum sociis natoque penatibus et magnis dis parturient montes, nascetur ridiculus mus. Donec quam felis, ultricies nec, pellen.</p>
</section>
<div class="intro-pointer abs"></div>

<div class="iconbox abs" style="left:90px">
  <div class="ring"><svg width="26" height="26" viewBox="0 0 26 26"><circle cx="13" cy="8" r="5.5" fill="var(--blue-dark)"/><path d="M3 24c0-6 4-9 10-9s10 3 10 9z" fill="var(--blue-dark)"/></svg></div>
  <h3>ICONBOX TITLE</h3>
  <p>Aenean e penatibus et magnis dis parturient montes, nascetur ridiculus mus. Lorem ipsum dolor sit amet, consectetuer adipiscing elit.</p>
</div>
<div class="iconbox abs" style="left:439px">
  <div class="ring"><svg width="28" height="28" viewBox="0 0 28 28" stroke="#333" stroke-width="2.6" stroke-linecap="round"><line x1="6" y1="22" x2="20" y2="8"/><line x1="6" y1="6" x2="22" y2="22"/><circle cx="21" cy="7" r="3" fill="none"/></svg></div>
  <h3>ICONBOX TITLE</h3>
  <p>Aenean e penatibus et magnis dis parturient montes, nascetur ridiculus mus. Lorem ipsum dolor sit amet, consectetuer adipiscing elit.</p>
</div>
<div class="iconbox abs" style="left:788px">
  <div class="ring"><svg width="26" height="26" viewBox="0 0 26 26"><path d="M13 2l3.3 7 7.7.9-5.7 5.2 1.6 7.6L13 18.9 6.1 22.7l1.6-7.6L2 9.9 9.7 9z" fill="var(--blue-dark)"/></svg></div>
  <h3>ICONBOX TITLE</h3>
  <p>Aenean e penatibus et magnis dis parturient montes, nascetur ridiculus mus. Lorem ipsum dolor sit amet, consectetuer adipiscing elit.</p>
</div>

<article class="card abs" style="left:98px;width:311px">
  <div class="photo" role="img" aria-label="Photo of a laptop and tablet on a wooden desk" style="background:linear-gradient(135deg,#3a3028,#8a8580 55%,#d8d2c8)"></div>
  <div class="badge"><svg width="34" height="30" viewBox="0 0 34 30" fill="#fff"><rect x="10" y="2" width="13" height="11"/><rect x="2" y="16" width="13" height="11"/><rect x="19" y="16" width="13" height="11"/></svg></div>
  <h4>Development</h4>
  <p>Int curletus eger porta nisl vitae fetrum ut molm he nae felis rutrum.</p>
</article>
<article class="card abs" style="left:436px;width:323px">
  <div class="photo" role="img" aria-label="Photo of an empty boardroom table with chairs" style="background:linear-gradient(160deg,#e8e8e8,#9a9a9a 50%,#2e2e2e)"></div>
  <div class="badge"><svg width="32" height="30" viewBox="0 0 32 30" fill="#fff"><rect x="12" y="2" width="8" height="7"/><rect x="2" y="21" width="8" height="7"/><rect x="12" y="21" width="8" height="7"/><rect x="22" y="21" width="8" height="7"/><path d="M15 9h2v5h10v7h-2v-5h-8v5h-2v-5H7v5H5v-7h10z"/></svg></div>
  <h4>Motion Design</h4>
  <p>Int curletus eger porta nisl vitae fetrum ut molm he nae felis rutrum.</p>
</article>
<article class="card abs" style="left:786px;width:311px">
  <div class="photo" role="img" aria-label="Photo of city skyscrapers in haze" style="background:linear-gradient(90deg,#4a4e55,#a9adb2 45%,#c8cbcf 60%,#2c3038)"></div>
  <div class="badge"><svg width="28" height="28" viewBox="0 0 28 28" fill="#fff"><circle cx="20" cy="6" r="4.5"/><circle cx="7" cy="14" r="4.5"/><circle cx="20" cy="22" r="4.5"/><path d="M7 14L20 6M7 14l13 8" stroke="#fff" stroke-width="2.5"/></svg></div>
  <h4>Marketing Strategies</h4>
  <p>Int curletus eger porta nisl vitae fetrum ut molm he nae felis rutrum.</p>
</article>

<section class="testimonial abs">
  <h5>Mark Ellison of Brightwell Training</h5>
  <p>Aenean placerat tortor ac dui luctus ut mattis est mollis. Donec blandit orci id velit cursus varius. Fusce quam enim, hendrerit nec ultrices a, vestibulum nec enim. Quisque im-perdiet ultricies dolor in convallis. Morbi sed fringilla elit. Duis sagittis lectus in orci volut-pat elementum. Cras in purus sem. Curabitur augue velit, mollis in suscipit eleifend, fauci</p>
</section>
<div class="avatar abs" role="img" aria-label="Portrait photo of the client"></div>

<div class="step-line abs"></div>
<div class="step-ring abs" style="top:1593px"><svg width="34" height="34" viewBox="0 0 34 34" fill="none" stroke="#888" stroke-width="2"><rect x="4" y="7" width="26" height="23" rx="2"/><line x1="4" y1="13" x2="30" y2="13"/><line x1="11" y1="3" x2="11" y2="9"/><line x1="23" y1="3" x2="23" y2="9"/><path d="M9 18h4M15 18h4M21 18h4M9 24h4M15 24h4M21 24h4"/></svg></div>
<div class="step-ring abs" style="top:1741px"><svg width="32" height="32" viewBox="0 0 32 32" fill="#888"><path d="M22 3l7 7-16 16-8 2 2-8z"/></svg></div>
<div class="step-ring abs" style="top:1890px"><svg width="36" height="32" viewBox="0 0 36 32" fill="none" stroke="#888" stroke-width="2.4"><rect x="3" y="3" width="30" height="20" rx="1"/><path d="M14 23l-2 6M22 23l2 6M10 29h16"/></svg></div>

<div class="step abs" style="top:1590px"><h4>Planning</h4><p>The planning stage is arguably the most important, because what’s decided and mapped here sets the stage for the entire project. This is also the stage that requires client interaction and the accompanying attention to detail.</p></div>
<div class="step abs" style="top:1739px"><h4>Design</h4><p>The design stage typically involves moving the information outlined in the planning stage further into reality. The main deliverables are a documented site structure and, more importantly, a visual representation.</p></div>
<div class="step abs" style="top:1888px"><h4>Development</h4><p>Development involves the bulk of the programming work, as well as loading content (whether by your team or the client’s). Keep code organized and commented, and refer constantly to the planning details as the full website takes shape.</p></div>

<footer class="site-footer abs">
  <h2 style="left:114px">NEWSLETTER</h2>
  <p class="news-text abs">Lorem Ipsum is simply dummy text of the printing and typesetting industry.</p>
  <div class="news-form abs"><div class="news-input">Your Email</div><div class="news-btn">Subscribe</div></div>
  <div class="social abs"><span></span><span></span><span></span><span></span><span></span></div>

  <h2 style="left:515px">LOCATIONS</h2>
  <div class="loc abs" style="top:82px"><svg width="14" height="20" viewBox="0 0 14 20"><path d="M7 0a7 7 0 0 1 7 7c0 5-7 13-7 13S0 12 0 7a7 7 0 0 1 7-7z" fill="#ddd"/><circle cx="7" cy="7" r="2.5" fill="#2b2b2b"/></svg><div>118 Harbour Rd, Northgate WA 6001<br>Phone: +61 8 5550 2140</div></div>
  <div class="loc abs" style="top:132px"><svg width="14" height="20" viewBox="0 0 14 20"><path d="M7 0a7 7 0 0 1 7 7c0 5-7 13-7 13S0 12 0 7a7 7 0 0 1 7-7z" fill="#999"/><circle cx="7" cy="7" r="2.5" fill="#2b2b2b"/></svg><div>42 Quarry St, Eastbrook WA 6004<br>Phone: +61 8 5550 2286</div></div>
  <div class="loc abs" style="top:182px"><svg width="14" height="20" viewBox="0 0 14 20"><path d="M7 0a7 7 0 0 1 7 7c0 5-7 13-7 13S0 12 0 7a7 7 0 0 1 7-7z" fill="#999"/><circle cx="7" cy="7" r="2.5" fill="#2b2b2b"/></svg><div>9 Mill Lane, Southmere WA 6010<br>Phone: +61 8 5550 2391</div></div>

  <h2 style="left:864px">LATEST TWEETS</h2>
  <span class="tweet-dot abs"></span>
  <p class="tweet abs">New planning guide out now for small teams, read the full checklist on our blog today.</p>
  <div class="tweet-meta abs"><span>5 hours ago</span><span>More</span></div>
</footer>
<div class="copyright abs">Copyright 2014 @ tarnvaleadvisory.com</div>

</body>
</html>
```